Proposal Poster, posters for kids to hold

I am proposing to my girlfriend soon, I need two posters made for my kids to hold one I want to say “be my mommy”
And the other “will you marry my daddy”
Both in horizontal format. I plan on sending the files to a print shop to get them printed on a large poster. Simple is fine with maybe a few graphics. Open to anything. Kids will be holding it from the beach as we are on a jet ski close to shore. Must be readable font from a short distance

• Cute but readable font from a distance

```html
<!DOCTYPE html>
<html lang="en">
<head>
<meta charset="utf-8">
<title>Be My Mommy – Proposal Poster</title>
<link href="https://fonts.googleapis.com/css2?family=Lobster&family=Lobster+Two:wght@700&family=Lilita+One&display=swap" rel="stylesheet">
<style>
  :root {
    --page-bg: #e8e8e8;
    --poster-pink-light: #fdf1f8;
    --poster-pink: #f8cfe6;
    --ink-slate: #58628a;
    --ink-navy: #324a8f;
    --ink-red: #f0284a;
    --heart-red: #c8143c;
    --swoosh-black: #1d1d1f;
    --art-blue-1: #6fb6f2;
    --art-blue-2: #2f7fd6;
    --art-peach-1: #fdf0e6;
    --art-peach-2: #f3c9b8;
  }
  html, body {
    margin: 0;
    width: 798px;
    height: 1200px;
    overflow: hidden;
    background: var(--page-bg);
  }
  .poster {
    position: absolute;
    left: 29px;
    top: 323px;
    width: 740px;
    height: 554px;
    box-shadow: 0 3px 6px rgba(0,0,0,.35);
  }
  .poster svg { display: block; width: 100%; height: 100%; }
  .word-be { font-family: "Lobster Two", cursive; font-weight: 700; fill: var(--ink-slate); }
  .word-my { font-family: "Lilita One", sans-serif; fill: var(--ink-navy); }
  .word-mommy { font-family: "Lobster", cursive; fill: var(--ink-red); }
</style>
</head>
<body>
<div class="poster">
  <svg viewBox="0 0 1244 932" xmlns="http://www.w3.org/2000/svg">
    <defs>
      <radialGradient id="poster-bg" cx="50%" cy="50%" r="75%">
        <stop offset="0%" stop-color="var(--poster-pink-light)"/>
        <stop offset="100%" stop-color="var(--poster-pink)"/>
      </radialGradient>
      <linearGradient id="art-blue" x1="0" y1="0" x2="1" y2="1">
        <stop offset="0%" stop-color="var(--art-blue-1)"/>
        <stop offset="100%" stop-color="var(--art-blue-2)"/>
      </linearGradient>
      <radialGradient id="art-peach" cx="50%" cy="45%" r="60%">
        <stop offset="0%" stop-color="var(--art-peach-1)"/>
        <stop offset="100%" stop-color="var(--art-peach-2)"/>
      </radialGradient>
    </defs>

    <rect class="poster-background" width="1244" height="932" fill="url(#poster-bg)"/>

    <path class="art-mother-child-heart" role="img" aria-label="Illustration of a mother lifting her child inside a blue heart"
      d="M260 330 C160 270 100 210 100 135 C100 80 145 45 195 50 C230 54 255 75 262 100 C272 70 300 48 340 50 C390 54 420 95 412 145 C404 215 340 275 260 330 Z"
      fill="url(#art-blue)"/>

    <path class="art-mother-son-flowers" role="img" aria-label="Illustration of a mother hugging her son framed with flowers"
      d="M1040 50 C1120 50 1190 110 1190 190 C1190 260 1160 320 1090 345 C1050 360 960 360 905 330 C860 300 850 250 860 195 C875 110 960 50 1040 50 Z"
      fill="url(#art-peach)"/>

    <text class="word-be" x="665" y="272" text-anchor="middle" font-size="300">Be</text>
    <text class="word-my" x="680" y="560" text-anchor="middle" font-size="300" transform="translate(680 560) scale(0.9 1.05) translate(-680 -560)">My</text>
    <text class="word-mommy" x="600" y="800" text-anchor="middle" font-size="300">Mommy</text>

    <path class="heart" d="M400 440 C380 420 345 400 355 375 C363 357 388 356 400 375 C412 356 440 357 446 378 C452 402 420 422 400 440 Z" fill="var(--heart-red)"/>
    <path class="heart" d="M845 385 C832 372 815 362 820 348 C825 338 838 337 845 348 C852 337 867 338 870 350 C873 364 858 374 845 385 Z" fill="var(--heart-red)"/>
    <path class="heart heart-outline" d="M950 495 C930 470 905 450 918 425 C928 408 950 412 955 432 C968 410 1000 412 1005 432 C1010 455 980 475 950 495 Z" fill="none" stroke="var(--heart-red)" stroke-width="5"/>

    <g class="swoosh swoosh-left">
      <path d="M78 338 C140 340 195 370 222 432 C180 395 130 365 78 338 Z" fill="var(--ink-red)"/>
      <path d="M78 345 C135 352 180 380 212 428 C170 398 125 370 78 345 Z" fill="var(--swoosh-black)"/>
      <path d="M76 418 C120 410 165 418 195 438 C155 430 115 426 76 418 Z" fill="var(--ink-red)"/>
      <path d="M76 422 C118 418 160 424 190 440 C150 434 112 430 76 422 Z" fill="var(--swoosh-black)"/>
    </g>
    <g class="swoosh swoosh-right">
      <path d="M995 560 C1040 500 1110 455 1200 448 C1120 475 1050 515 995 560 Z" fill="var(--ink-red)"/>
      <path d="M1005 555 C1050 505 1110 468 1195 455 C1120 485 1060 520 1005 555 Z" fill="var(--swoosh-black)"/>
      <path d="M1030 566 C1080 545 1140 538 1200 548 C1140 552 1085 560 1030 566 Z" fill="var(--ink-red)"/>
      <path d="M1035 570 C1085 552 1140 548 1198 556 C1140 560 1088 566 1035 570 Z" fill="var(--swoosh-black)"/>
    </g>
    <g class="swoosh swoosh-bottom">
      <path d="M1075 800 C1110 825 1160 845 1200 880 C1150 860 1105 835 1075 800 Z" fill="var(--swoosh-black)"/>
      <path d="M1095 800 C1130 808 1170 810 1200 818 C1160 822 1125 815 1095 800 Z" fill="var(--ink-red)"/>
      <path d="M1098 805 C1135 812 1170 815 1200 824 C1160 826 1128 820 1098 805 Z" fill="var(--swoosh-black)"/>
    </g>
  </svg>
</div>
</body>
</html>
```